Fairbrook's Vacation Rentals Business Card

Multi Million dollar villa rentals in the Dominican Republic.

Industry/Entity Type

Business

Contact Information for Business Card

I am looking for a high-end look around my company name/logo (see attached) on one side incorporating the following info: first and last name, title, address, phone #, email and company website. On the backside I want to add a full color picture of one of our villas (see attached).

```html
<!DOCTYPE html>
<html lang="en">
<head>
<meta charset="utf-8">
<title>Fairbrook's Vacation Rentals – Business Card</title>
<link href="https://fonts.googleapis.com/css2?family=Open+Sans:wght@400;600&display=swap" rel="stylesheet">
<style>
  :root {
    --backdrop: #e4e4e2;
    --card: #f4f4f2;
    --ink: #4a4a4a;
    --accent: #f07a1e;
    --pool: #2aa3e0;
    --sky: #6fb3e8;
    --stucco: #e9e6df;
    --roof: #c8643f;
  }
  * { margin: 0; padding: 0; box-sizing: border-box; }
  html, body { width: 1200px; height: 1200px; overflow: hidden; }
  body {
    background: var(--backdrop);
    font-family: "Open Sans", sans-serif;
    color: var(--ink);
    display: flex;
    flex-direction: column;
    align-items: center;
    justify-content: center;
    gap: 52px;
  }
  .card {
    width: 900px;
    height: 514px;
    background: var(--card);
    box-shadow: 0 6px 18px rgba(0,0,0,0.15);
    position: relative;
  }
  .brand {
    position: absolute;
    left: 70px;
    top: 80px;
    display: flex;
    align-items: center;
    gap: 16px;
  }
  .brand-dot {
    width: 54px; height: 54px;
    border-radius: 50%;
    background: var(--accent);
  }
  .brand-name {
    font-weight: 600;
    font-size: 30px;
    color: var(--accent);
    letter-spacing: 0.2px;
  }
  .contact {
    position: absolute;
    left: 430px;
    top: 200px;
    font-size: 19px;
    line-height: 1.5;
  }
  .contact-name {
    font-weight: 600;
    font-size: 22px;
    letter-spacing: 0.5px;
    margin-bottom: 16px;
  }
  .contact-line {
    display: flex;
    align-items: center;
    gap: 12px;
  }
  .contact-line svg { width: 18px; height: 18px; flex: none; }
  .address { margin-top: 14px; max-width: 420px; }
  .card-back { padding: 22px; }
  .villa-photo {
    width: 100%;
    height: 100%;
    background: linear-gradient(180deg, var(--sky) 0%, var(--roof) 14%, var(--stucco) 22%, var(--stucco) 62%, var(--pool) 72%, #1b86c7 100%);
  }
</style>
</head>
<body>
  <section class="card card-front">
    <div class="brand">
      <span class="brand-dot"></span>
      <span class="brand-name">Fairbrook's Vacation Rentals</span>
    </div>
    <div class="contact">
      <p class="contact-name">MARCO LINDQVIST - CEO</p>
      <p class="contact-line">
        <svg viewBox="0 0 18 18" aria-hidden="true"><rect x="4" y="1" width="10" height="16" rx="2" fill="none" stroke="var(--accent)" stroke-width="2"/><circle cx="9" cy="14" r="1" fill="var(--accent)"/></svg>
        +00 11 222 3344
      </p>
      <p class="contact-line">
        <svg viewBox="0 0 18 18" aria-hidden="true"><rect x="1" y="3" width="16" height="12" fill="none" stroke="var(--accent)" stroke-width="2"/><path d="M1 4 L9 10 L17 4" fill="none" stroke="var(--accent)" stroke-width="2"/></svg>
        marco@fairbrookvacations.com
      </p>
      <p class="contact-line">
        <svg viewBox="0 0 18 18" aria-hidden="true"><circle cx="9" cy="9" r="8" fill="var(--accent)"/><path d="M1 9 H17 M9 1 V17 M3 5 H15 M3 13 H15" stroke="var(--card)" stroke-width="1"/></svg>
        www.fairbrookvacations.com
      </p>
      <p class="address">#14, Palmera Bldg, Dominican Republic onum imus ex et, apellab ipsapid esti odicietusci a es exerovitis.</p>
    </div>
  </section>

  <section class="card card-back">
    <div class="villa-photo" role="img" aria-label="Photo of a white colonnaded villa with red tile roof, balcony railings, palm trees and a blue pool lined with blue loungers"></div>
  </section>
</body>
</html>
```